Environmentally friendly carpet cleaning postcard/flyer

Wexamora is an environmentally friendly carpet rug and upholstery cleaner (servicing both residential and commercial customers). We are new to the Southern California market, although there is a franchise located in Northern California that has been operating for a few years. Our website is wwww.TRZephyrPip.com - we opened in November 2013 and have been growing but need to develop a post card that highlights our uniqueness to our key customers- families with young children and pet parents. We need a postcard, flyer, or door hanger but something that we can hand out or place under door mats, etc, or have with us during a farmers market, etc.
Updates

Added new citrus graphic

Thank You all for participating- I will be sure to use pixel bazaar again in the future.

Target Market(s)

stay at home moms or busy moms with children; and pet parents

Industry/Entity Type

Residential

Requirements
Must have
• should include the tall zephyr pip and potentially some citrus graphics - please do not take the images or docs that I posted as our "inspiration" as we are looking for some creativity and changes to what we have been using. Something professional, more upscale than the traditional carpet cleaning promotion flyer - our prices are fixed prices, we don't change them by the job and we have them posted on our website. Our market is in San Diego from coastal Del Mar (92014) to inland Poway (92064).

```html
<!DOCTYPE html>
<html lang="en">
<head>
<meta charset="utf-8">
<title>Wexamora Postcard</title>
<link rel="stylesheet" href="https://fonts.googleapis.com/css2?family=Nunito:wght@400;600;700;800&display=swap">
<style>
  :root {
    --paper: #f7f7f7;
    --carpet: #e9e7e1;
    --carpet-shade: #dcd9d2;
    --red: #e8334d;
    --red-dark: #c9233c;
    --orange: #e8901e;
    --green: #8fbf2e;
    --white: #ffffff;
    --ink: #333333;
    --rule: #d8d8d8;
    --stamp-border: #cfcfcf;
    --icon-blue: #2f66c4;
    --tile-top: #ffffff;
    --tile-bottom: #d9d9d9;
  }
  * { margin: 0; padding: 0; box-sizing: border-box; }
  html, body {
    width: 1200px; height: 930px; overflow: hidden;
    background: var(--paper);
    font-family: "Nunito", sans-serif;
  }
  .postcard { position: relative; width: 1200px; height: 930px; background: var(--paper); }

  .front-panel { position: absolute; left: 0; top: 0; width: 579px; height: 765px; overflow: hidden; }
  .carpet-photo {
    position: absolute; inset: 0;
    background: radial-gradient(circle at 40% 60%, var(--carpet) 0%, var(--carpet-shade) 100%);
  }

  .contact-box {
    position: absolute; left: 28px; top: 0; width: 388px; height: 215px;
    background: linear-gradient(180deg, var(--red) 0%, var(--red-dark) 100%);
    box-shadow: 0 4px 10px rgba(0,0,0,0.25);
    padding: 60px 0 0 24px;
  }
  .contact-line {
    display: flex; align-items: center; gap: 8px;
    color: var(--white); font-weight: 700; font-size: 28px; line-height: 44px;
    text-shadow: 0 1px 2px rgba(0,0,0,0.3);
  }
  .contact-line svg { width: 22px; height: 22px; flex: none; }

  .hours-band {
    position: absolute; left: 0; top: 361px; width: 579px; height: 104px;
    background: var(--orange);
    padding: 19px 0 0 40px;
    color: var(--white); font-weight: 700; font-size: 22px; line-height: 28px;
    text-shadow: 0 1px 2px rgba(0,0,0,0.25);
  }
  .schedule-band {
    position: absolute; left: 0; top: 465px; width: 579px; height: 87px;
    background: var(--green);
    box-shadow: 0 3px 6px rgba(0,0,0,0.2);
  }
  .schedule-band .call {
    position: absolute; left: 176px; top: 24px;
    color: var(--white); font-weight: 700; font-size: 27px;
    text-shadow: 0 1px 2px rgba(0,0,0,0.25);
  }

  .service-tile {
    position: absolute;
    background: linear-gradient(180deg, var(--tile-top) 0%, var(--tile-bottom) 100%);
    box-shadow: 0 3px 8px rgba(0,0,0,0.35);
    display: flex; flex-direction: column; justify-content: center; align-items: center;
    font-weight: 700; line-height: 1;
  }
  .service-tile .kind { font-size: 21px; }
  .service-tile .word { font-size: 29px; }
  .tile-residential { left: 420px; top: 360px; width: 138px; height: 105px; color: var(--orange); }
  .tile-commercial { left: 25px; top: 444px; width: 138px; height: 108px; color: var(--green); }

  .cta {
    position: absolute; left: 0; top: 672px; width: 558px;
    text-align: center; color: var(--ink); font-size: 30px; font-weight: 600; line-height: 35px;
  }

  .stamp-box {
    position: absolute; left: 904px; top: 31px; width: 264px; height: 265px;
    background: var(--white); border: 2px solid var(--stamp-border);
  }
  .address-line {
    position: absolute; left: 645px; width: 494px; height: 2px; background: var(--rule);
  }
</style>
</head>
<body>
<div class="postcard">
  <section class="front-panel">
    <div class="carpet-photo" role="img" aria-label="Close-up photo of clean white carpet fibers"></div>

    <div class="contact-box">
      <div class="contact-line">
        <svg viewBox="0 0 22 22"><circle cx="11" cy="11" r="10" fill="var(--icon-blue)" stroke="#fff" stroke-width="1.5"/><circle cx="11" cy="11" r="5" fill="none" stroke="#fff" stroke-width="1.5"/><line x1="6" y1="11" x2="16" y2="11" stroke="#fff" stroke-width="1.2"/></svg>
        www.trzephyrpip.com
      </div>
      <div class="contact-line">
        <svg viewBox="0 0 22 22"><circle cx="11" cy="11" r="10" fill="var(--icon-blue)" stroke="#fff" stroke-width="1.5"/><path d="M8 6 L10 6 L10.5 9 L9.2 10 Q10 12.5 12 13.8 L13 12.5 L16 13 L16 15 Q12 16.5 8.5 12.5 Q6.5 9.5 8 6 Z" fill="#fff"/></svg>
        858-555-0143
      </div>
      <div class="contact-line">
        <svg viewBox="0 0 22 22"><circle cx="11" cy="11" r="10" fill="var(--icon-blue)" stroke="#fff" stroke-width="1.5"/><text x="11" y="15.5" text-anchor="middle" font-size="13" font-weight="700" fill="#fff" font-family="Nunito, sans-serif">@</text></svg>
        wx52@wexamora.com
      </div>
    </div>

    <div class="hours-band">
      <p>Monday - Friday: 8:00am to 7:00pm</p>
      <p>Saturday: 8:00am to 12:00pm</p>
    </div>
    <div class="schedule-band">
      <span class="call">Call to schedule</span>
    </div>

    <div class="service-tile tile-residential">
      <span class="kind">Residential</span>
      <span class="word">Cleaning</span>
    </div>
    <div class="service-tile tile-commercial">
      <span class="kind">Commercial</span>
      <span class="word">Cleaning</span>
    </div>

    <p class="cta">Call, text or email us to schedule<br>your appointment today</p>
  </section>

  <div class="stamp-box"></div>
  <div class="address-line" style="top:416px"></div>
  <div class="address-line" style="top:500px"></div>
  <div class="address-line" style="top:582px"></div>
  <div class="address-line" style="top:663px"></div>
</div>
</body>
</html>
```